Poster Required for Cafe to promote Catering

I would like a Poster made to advertise that our business does catering.
On the poster we would like it to say:

Did you know that Lantern Pantry does Catering?
We offer Breakfast, Lunch, Morning and Afternoon Tea Options
Come instore to enquire

At the bottom of the flyer, can you please put the contact details:
Phone 0472 918 604
Email mia@lanternpantrykitchen.com

Poster Size A3

I have attached our logo and menu's so you can get a feel for what we like.

Target Market(s)

Hospital Staff: Doctors, Nurses, Admin

Industry/Entity Type

Hospitality

Requirements
Nice to have
• Some pictures of catering. Eg. Gourmet Sandwiches, Sliders
• You could check our instagram page for ideas on what we do..
• @lntpantry_qld

```html
<!DOCTYPE html>
<html lang="en">
<head>
<meta charset="utf-8">
<title>Lantern Pantry Catering Poster</title>
<link rel="stylesheet" href="https://fonts.googleapis.com/css2?family=Yellowtail&family=Cutive+Mono&family=Josefin+Sans:wght@400&display=swap">
<style>
  :root {
    --page-bg: #ffffff;
    --orange-deep: #e67b1a;
    --orange-mid: #f29a14;
    --orange-light: #f8c21c;
    --ink-brown: #3b2b26;
    --paper-white: #ffffff;
    --photo-cream: #eee7dc;
    --photo-green: #7f9a45;
    --photo-amber: #b7743a;
    --food-bread: #d9a566;
    --food-board: #e9cf9a;
  }
  * { box-sizing: border-box; margin: 0; padding: 0; }
  html, body {
    width: 1200px;
    height: 900px;
    overflow: hidden;
    background: var(--page-bg);
  }
  .canvas {
    position: relative;
    width: 1200px;
    height: 900px;
  }
  .poster {
    position: absolute;
    left: 296px;
    top: 20px;
    width: 608px;
    height: 860px;
    overflow: hidden;
    background: radial-gradient(ellipse 75% 60% at 50% 45%, var(--orange-light) 0%, var(--orange-mid) 55%, var(--orange-deep) 100%);
    box-shadow: 0 2px 10px rgba(0,0,0,0.18);
  }

  /* Brand header */
  .brand {
    position: absolute;
    top: 78px;
    left: 0;
    width: 100%;
    display: flex;
    align-items: center;
    justify-content: center;
    gap: 18px;
  }
  .brand-rule {
    width: 92px;
    height: 2px;
    background: var(--ink-brown);
  }
  .brand-mark {
    width: 26px;
    height: 26px;
    border-radius: 50%;
    background: var(--ink-brown);
  }
  .brand-name {
    font-family: "Yellowtail", cursive;
    font-size: 34px;
    color: var(--ink-brown);
    line-height: 1;
  }

  .headline {
    position: absolute;
    top: 168px;
    left: 40px;
    right: 40px;
    text-align: center;
    font-family: "Yellowtail", cursive;
    font-size: 40px;
    line-height: 1.05;
    color: var(--ink-brown);
  }

  .banquet-photo {
    position: absolute;
    top: 270px;
    left: 0;
    width: 608px;
    height: 300px;
  }

  /* Offer section */
  .offer-title {
    position: absolute;
    top: 574px;
    left: 0;
    width: 100%;
    display: flex;
    align-items: center;
    justify-content: center;
    gap: 16px;
    font-family: "Yellowtail", cursive;
    font-size: 28px;
    color: var(--ink-brown);
  }
  .offer-rule {
    width: 88px;
    height: 2px;
    background: var(--ink-brown);
  }
  .offer-list {
    position: absolute;
    top: 614px;
    left: 0;
    width: 100%;
    text-align: center;
    font-family: "Yellowtail", cursive;
    font-size: 21px;
    color: var(--ink-brown);
  }

  .platter-photo {
    position: absolute;
    top: 646px;
    left: 40px;
    width: 528px;
    height: 130px;
  }

  .contact {
    position: absolute;
    left: 0;
    width: 100%;
    text-align: center;
    font-family: "Cutive Mono", monospace;
    color: var(--paper-white);
  }
  .contact-phone {
    top: 792px;
    font-size: 18px;
    letter-spacing: 4px;
  }
  .contact-email {
    top: 822px;
    font-size: 15px;
    letter-spacing: 3px;
  }
</style>
</head>
<body>
<main class="canvas">
  <article class="poster">
    <header class="brand">
      <span class="brand-rule"></span>
      <span class="brand-mark"></span>
      <span class="brand-name">Lantern Pantry</span>
      <span class="brand-rule"></span>
    </header>

    <h1 class="headline">Did you know that Lantern Pantry does Catering?</h1>

    <svg class="banquet-photo" viewBox="0 0 608 300" role="img" aria-label="Photograph of a catered banquet table with glassware and a salad platter">
      <defs>
        <linearGradient id="banquetTone" x1="0" y1="0" x2="0" y2="1">
          <stop offset="0" stop-color="var(--photo-amber)"/>
          <stop offset="0.35" stop-color="var(--photo-cream)"/>
          <stop offset="0.6" stop-color="var(--photo-green)"/>
          <stop offset="1" stop-color="var(--photo-cream)"/>
        </linearGradient>
      </defs>
      <path d="M0 52 Q304 2 608 40 L608 262 Q430 252 300 280 Q150 300 0 266 Z" fill="url(#banquetTone)"/>
      <path d="M0 52 Q304 2 608 40" fill="none" stroke="var(--paper-white)" stroke-width="6"/>
      <path d="M0 266 Q150 300 300 280 Q430 252 608 262" fill="none" stroke="var(--paper-white)" stroke-width="6"/>
    </svg>

    <div class="offer-title">
      <span class="offer-rule"></span>
      <span>We Offer</span>
      <span class="offer-rule"></span>
    </div>
    <p class="offer-list">Breakfast, Lunch, Morning and Afternoon Tea Options</p>

    <svg class="platter-photo" viewBox="0 0 528 130" role="img" aria-label="Photograph of a gourmet sandwich, three sliders on a wooden board and two cupcakes">
      <defs>
        <linearGradient id="platterTone" x1="0" y1="0" x2="1" y2="0">
          <stop offset="0" stop-color="var(--food-bread)"/>
          <stop offset="0.7" stop-color="var(--food-board)"/>
          <stop offset="1" stop-color="#e58fa6"/>
        </linearGradient>
      </defs>
      <rect x="0" y="10" width="528" height="110" rx="22" fill="url(#platterTone)" opacity="0.9"/>
    </svg>

    <p class="contact contact-phone">0472 918 604</p>
    <p class="contact contact-email">Email: mia@lanternpantrykitchen.com</p>
  </article>
</main>
</body>
</html>
```